Mobile Oil Change company needs a flyer to promote new business

We need a flyer to 1) print & handout and 2) email out to potential customers. We are a mobile oil change company that comes to our customer locations to perform the work instead of customers going to traditional oil change companies. We have a 21 point inspection with our oil change. (21 point inspection details will not be on the flyer). Would like to keep the flyer simple but creative. I'm attaching 1) the write-up we created, 2) our logo (logo color is dark teal on white but other combinations are included if you wanted to propose a different color combination), and 3) additional services we offer. Logo font is Alegreya Sans.
Would like the additional services listed with icons and brief descriptions (similar to attachment) without pricing. Company website for reference is www.brindlefleetcare.com.

Target Market(s)

Companies with many service vehicles such as Oil & Gas service companies, heating and air conditioning companies, utility companies, police departments, etc. Companies that prioritize convenience and maintenance first.

Font styles to use
Sans Serif

Colors
00a990

Requirements
Must have
• Simple but creative design with our logo at top of the flyer. Additional Services (details in document supplied) can be smaller and less prominent than other "main" content listed in the CONTENT document supplied.
Should not have
• Do not use animated character graphics in the flyer and limit (1) stock photos to A small area in the flyer.

```html
<!DOCTYPE html>
<html lang="en">
<head>
<meta charset="utf-8">
<title>Brindle Fleet Care – Mobile Oil Change Flyer</title>
<link rel="stylesheet" href="https://fonts.googleapis.com/css2?family=Roboto:wght@700&family=Roboto+Condensed:wght@400;500;700&family=Source+Sans+3:wght@400;600&display=swap">
<style>
  :root{
    --teal:#17a58c;
    --teal-bright:#1fb39a;
    --teal-deep:#1b4a4d;
    --ink:#24484b;
    --grey-text:#4d5254;
    --white:#ffffff;
  }
  *{margin:0;padding:0;box-sizing:border-box}
  html,body{width:978px;height:1200px;overflow:hidden;background:var(--white)}
  .flyer{position:relative;width:978px;height:1200px;background:var(--white);font-family:"Source Sans 3",sans-serif}

  .hero{position:absolute;left:32px;top:31px;width:918px;height:544px;border-top-left-radius:70px;overflow:hidden;
    background:
      radial-gradient(ellipse 150px 240px at 82% 45%, rgba(236,180,30,.75), transparent 70%),
      radial-gradient(ellipse 300px 200px at 60% 20%, rgba(80,110,160,.55), transparent 75%),
      linear-gradient(100deg,#121820 0%,#1e2836 45%,#2f4260 75%,#8c98a8 100%)}
  .hero-shade{position:absolute;inset:0;background:linear-gradient(90deg,rgba(10,14,20,.8) 0%,rgba(10,14,20,.45) 45%,transparent 70%)}

  .brand{position:absolute;left:78px;top:104px;display:flex;align-items:center;gap:12px;
    font-weight:600;font-size:36px;line-height:44px;color:var(--teal-bright);letter-spacing:1px}
  .brand-mark{width:22px;height:22px;background:var(--teal-bright)}

  .headline{position:absolute;left:64px;top:213px;font-family:"Roboto",sans-serif;font-weight:700;
    font-size:48px;line-height:55px;color:var(--white);letter-spacing:.5px}

  .perks{position:absolute;left:69px;top:405px;list-style:none;color:var(--white);font-size:21px;line-height:34px}
  .perks li{position:relative;padding-left:31px}
  .perks svg{position:absolute;left:0;top:7px}

  .services{position:absolute;left:499px;top:443px;width:479px;height:757px;background:var(--teal);border-top-left-radius:62px}
  .services-title{position:absolute;top:26px;left:82px;width:371px;text-align:center;white-space:nowrap;
    font-family:"Roboto Condensed",sans-serif;font-weight:700;font-size:38px;line-height:44px;color:var(--white)}

  .service{position:absolute;left:0;width:479px;height:92px}
  .service-icon{position:absolute;left:22px;top:-6px;width:88px;height:88px}
  .service-name{position:absolute;left:127px;top:0;width:323px;height:24px;background:var(--teal-deep);
    clip-path:polygon(0 0,96% 0,100% 100%,0 100%);white-space:nowrap;
    font-family:"Roboto Condensed",sans-serif;font-weight:500;font-size:20px;line-height:24px;color:var(--white);padding-left:8px}
  .service-desc{position:absolute;left:127px;top:25px;width:323px;font-family:"Roboto Condensed",sans-serif;
    font-size:17px;line-height:18.5px;color:var(--white);text-align:justify}

  .intro{position:absolute;left:37px;top:634px;width:455px;font-size:23px;line-height:34px;color:var(--ink);white-space:nowrap}
  .steps{position:absolute;left:44px;top:753px;width:440px;list-style:none;color:var(--grey-text);font-size:20px;line-height:38px;white-space:nowrap}
  .steps li{position:relative;padding-left:19px}
  .steps svg{position:absolute;left:0;top:12px}

  .cta{position:absolute;left:51px;top:1080px;font-family:"Roboto",sans-serif;font-weight:700;font-size:35px;line-height:42px;color:var(--teal-deep)}

  .contact-bar{position:absolute;left:23px;top:1137px;width:955px;height:51px;background:var(--teal-deep);
    border-radius:26px 0 0 26px;color:var(--white);font-weight:600;font-size:24px;line-height:51px}
  .contact-item{position:absolute;top:0;display:flex;align-items:center;gap:9px;height:51px;white-space:nowrap}
</style>
</head>
<body>
<main class="flyer">

  <section class="hero" role="img" aria-label="Photo of a technician working in an engine bay while golden motor oil pours from a bottle">
    <div class="hero-shade"></div>
  </section>

  <div class="brand"><span class="brand-mark"></span>Brindle Fleet Care</div>

  <h1 class="headline">HASSLE FREE<br>OIL CHANGES<br>ON YOUR TERMS</h1>

  <ul class="perks">
    <li><svg width="22" height="20" viewBox="0 0 22 20"><rect x="1" y="3" width="15" height="15" rx="2" fill="none" stroke="#1fb39a" stroke-width="2"/><path d="M5 10l4 4 11-12" fill="none" stroke="#1fb39a" stroke-width="2.4"/></svg>Service includes a 21-point inspection</li>
    <li><svg width="22" height="20" viewBox="0 0 22 20"><rect x="1" y="3" width="15" height="15" rx="2" fill="none" stroke="#1fb39a" stroke-width="2"/><path d="M5 10l4 4 11-12" fill="none" stroke="#1fb39a" stroke-width="2.4"/></svg>Additional services are available</li>
    <li><svg width="22" height="20" viewBox="0 0 22 20"><rect x="1" y="3" width="15" height="15" rx="2" fill="none" stroke="#1fb39a" stroke-width="2"/><path d="M5 10l4 4 11-12" fill="none" stroke="#1fb39a" stroke-width="2.4"/></svg>High quality synthetic oil used is best<br>suited for commercial vehicles</li>
  </ul>

  <section class="services">
    <h2 class="services-title">ADDITIONAL SERVICES</h2>

    <div class="service" style="top:100px">
      <svg class="service-icon" viewBox="0 0 88 88"><circle cx="44" cy="44" r="41" fill="#1fb39a" stroke="#fff" stroke-width="4"/><circle cx="44" cy="44" r="33" fill="none" stroke="#1b4a4d" stroke-width="1.5"/><rect x="28" y="26" width="32" height="36" fill="none" stroke="#1b4a4d" stroke-width="2.5"/><path d="M44 26v36M33 32h6M33 38h6M33 44h6M33 50h6M33 56h6M49 32h6M49 38h6M49 44h6M49 50h6M49 56h6" stroke="#1b4a4d" stroke-width="2"/></svg>
      <div class="service-name">ENGINE AIR FILTER REPLACEMENT</div>
      <p class="service-desc">Maintain optimum engine performace. Recomended every 15,000 to 30,000 miles.</p>
    </div>

    <div class="service" style="top:196px">
      <svg class="service-icon" viewBox="0 0 88 88"><circle cx="44" cy="44" r="41" fill="#1fb39a" stroke="#fff" stroke-width="4"/><circle cx="44" cy="44" r="33" fill="none" stroke="#1b4a4d" stroke-width="1.5"/><rect x="29" y="26" width="30" height="36" rx="3" fill="none" stroke="#1b4a4d" stroke-width="2.5"/><path d="M24 36q6-4 12 0t12 0 12 0 6 0M24 44q6-4 12 0t12 0 12 0 6 0M24 52q6-4 12 0t12 0 12 0 6 0" fill="none" stroke="#1b4a4d" stroke-width="2"/></svg>
      <div class="service-name">CABIN AIR FILTER REPLACEMENT</div>
      <p class="service-desc">Maintain a clean A/C and fan system. Recomended every 15,000 to 25,000 miles or 12 months.</p>
    </div>

    <div class="service" style="top:293px">
      <svg class="service-icon" viewBox="0 0 88 88"><circle cx="44" cy="44" r="41" fill="#1fb39a" stroke="#fff" stroke-width="4"/><circle cx="44" cy="44" r="33" fill="none" stroke="#1b4a4d" stroke-width="1.5"/><path d="M24 40q20-14 40 0L48 62H40z" fill="none" stroke="#1b4a4d" stroke-width="2.5"/><path d="M44 60L30 42" stroke="#1b4a4d" stroke-width="2.5"/><path d="M34 28h2M42 25h2M50 28h2" stroke="#1b4a4d" stroke-width="2"/></svg>
      <div class="service-name">WIPERBLADE REPLACEMENT</div>
      <p class="service-desc">Maintain excellent visability on the road. Recommended every 6 to 12 month.</p>
    </div>

    <div class="service" style="top:396px">
      <svg class="service-icon" viewBox="0 0 88 88"><circle cx="44" cy="44" r="41" fill="#1fb39a" stroke="#fff" stroke-width="4"/><circle cx="44" cy="44" r="33" fill="none" stroke="#1b4a4d" stroke-width="1.5"/><circle cx="44" cy="44" r="20" fill="none" stroke="#1b4a4d" stroke-width="3"/><circle cx="44" cy="46" r="5" fill="#1b4a4d"/><path d="M25 40q19 -6 38 0M44 51v13" stroke="#1b4a4d" stroke-width="3" fill="none"/></svg>
      <div class="service-name">POWER STEERING FLUID FLUSH</div>
      <p class="service-desc">Maintain proper power steering systetm health. Recomended every 30,000 to 60,000 miles</p>
    </div>

    <div class="service" style="top:504px">
      <svg class="service-icon" viewBox="0 0 88 88" style="top:-14px"><circle cx="44" cy="44" r="41" fill="#1fb39a" stroke="#fff" stroke-width="4"/><circle cx="44" cy="44" r="33" fill="none" stroke="#1b4a4d" stroke-width="1.5"/><rect x="30" y="26" width="20" height="36" rx="2" fill="none" stroke="#1b4a4d" stroke-width="2.5"/><rect x="34" y="31" width="12" height="9" fill="none" stroke="#1b4a4d" stroke-width="2"/><path d="M50 34l6 5v16q0 4 3 4t3-4V38l-4-6" fill="none" stroke="#1b4a4d" stroke-width="2.5"/><path d="M27 62h26" stroke="#1b4a4d" stroke-width="2.5"/></svg>
      <div class="service-name">FUEL SYSTEM TREATMENT</div>
      <p class="service-desc">Clean your fuel system and injectors to improve fuel economy.</p>
    </div>

    <div class="service" style="top:590px">
      <svg class="service-icon" viewBox="0 0 88 88" style="top:-1px"><circle cx="44" cy="44" r="41" fill="#1fb39a" stroke="#fff" stroke-width="4"/><circle cx="44" cy="44" r="33" fill="none" stroke="#1b4a4d" stroke-width="1.5"/><circle cx="44" cy="46" r="18" fill="none" stroke="#1b4a4d" stroke-width="2.5"/><circle cx="44" cy="46" r="6" fill="none" stroke="#1b4a4d" stroke-width="2.5"/><path d="M46 24a22 22 0 0 1 18 16l-6 2a16 16 0 0 0-12-12z" fill="#1b4a4d"/><circle cx="44" cy="36" r="1.6" fill="#1b4a4d"/><circle cx="34" cy="46" r="1.6" fill="#1b4a4d"/><circle cx="54" cy="46" r="1.6" fill="#1b4a4d"/><circle cx="44" cy="56" r="1.6" fill="#1b4a4d"/></svg>
      <div class="service-name">BRAKE FLUID FLUSH</div>
      <p class="service-desc">Maintain an excelent functioning brake system. Recomended every 20,000 miles or 2 years.</p>
    </div>
  </section>

  <p class="intro">Our simple 5-step process lets you schedule<br>an appointment and get service to save<br>time and money:</p>

  <ul class="steps">
    <li><svg width="15" height="15" viewBox="0 0 15 15"><circle cx="7.5" cy="7.5" r="6.5" fill="none" stroke="#17a58c" stroke-width="1.5"/><path d="M6 4.5l3 3-3 3" fill="none" stroke="#17a58c" stroke-width="1.6"/></svg>Call or email us to schedule service</li>
    <li><svg width="15" height="15" viewBox="0 0 15 15"><circle cx="7.5" cy="7.5" r="6.5" fill="none" stroke="#17a58c" stroke-width="1.5"/><path d="M6 4.5l3 3-3 3" fill="none" stroke="#17a58c" stroke-width="1.6"/></svg>Our highly trained technicians come to you<br>for service</li>
    <li><svg width="15" height="15" viewBox="0 0 15 15"><circle cx="7.5" cy="7.5" r="6.5" fill="none" stroke="#17a58c" stroke-width="1.5"/><path d="M6 4.5l3 3-3 3" fill="none" stroke="#17a58c" stroke-width="1.6"/></svg>Service is performed quickly on your vehicle</li>
    <li><svg width="15" height="15" viewBox="0 0 15 15"><circle cx="7.5" cy="7.5" r="6.5" fill="none" stroke="#17a58c" stroke-width="1.5"/><path d="M6 4.5l3 3-3 3" fill="none" stroke="#17a58c" stroke-width="1.6"/></svg>Pay agreed-upon pricing and receipt is<br>emailed to you</li>
    <li><svg width="15" height="15" viewBox="0 0 15 15"><circle cx="7.5" cy="7.5" r="6.5" fill="none" stroke="#17a58c" stroke-width="1.5"/><path d="M6 4.5l3 3-3 3" fill="none" stroke="#17a58c" stroke-width="1.6"/></svg>Services performed are tracked electronically<br>and reminders created</li>
  </ul>

  <h2 class="cta">CONTACT US TODAY!</h2>

  <footer class="contact-bar">
    <span class="contact-item" style="left:24px"><svg width="22" height="22" viewBox="0 0 22 22"><circle cx="11" cy="11" r="10" fill="none" stroke="#fff" stroke-width="1.6"/><rect x="5.5" y="7" width="11" height="8" fill="none" stroke="#fff" stroke-width="1.5"/><path d="M5.5 7l5.5 4.5L16.5 7" fill="none" stroke="#fff" stroke-width="1.5"/></svg>Sales@BrindleFleetCare.com</span>
    <span class="contact-item" style="left:404px"><svg width="22" height="22" viewBox="0 0 22 22"><circle cx="11" cy="11" r="10" fill="none" stroke="#fff" stroke-width="1.6"/><path d="M7 6l2.5-.5 1.2 3-1.5 1a7 7 0 0 0 3.3 3.3l1-1.5 3 1.2L16 15q-5 1-8-3T7 6z" fill="#fff"/></svg>(833) 555-0142</span>
    <span class="contact-item" style="left:668px"><svg width="22" height="22" viewBox="0 0 22 22"><circle cx="11" cy="11" r="10" fill="none" stroke="#fff" stroke-width="1.6"/><circle cx="11" cy="11" r="6.5" fill="none" stroke="#fff" stroke-width="1.2"/><ellipse cx="11" cy="11" rx="3" ry="6.5" fill="none" stroke="#fff" stroke-width="1.2"/><path d="M4.5 11h13M5.5 8h11M5.5 14h11" stroke="#fff" stroke-width="1"/></svg>BrindleFleetCare.com</span>
  </footer>

</main>
</body>
</html>
```